Ned Halvorsen Executive Coach Business Card Design

I need a new card design for my Executive Coaching practice. I am a Clinical Psychotherapist and Executive Coach. I help my clients get the most out of life by developing their personal and professional skills and abilities.

I work with senior executives. My design needs to be high end. I am thinking gloss on the front. I am also thinking contemporary. I am going to use a black, grey and red colour scheme on the the website. I am thinking grey with black and red accents. I would also like a water mark included on the card.

Target Market(s)

Senior Executives In major Companies

Industry/Entity Type

Business

Contact Information for Business Card

On the front

Ned Halvorsen
Clinical Psychotherapist and Executive Coach
For Personal and Professional Success

On the Back

Tarwin office
87 Tarwin Vale Road Tarwin

North Sydney Office
Suite 309 / 41 Lathom Street North Sydney

Pellington Street Office
Suite 512 / 218 Pellington Street Sydney CBD

Phone 02 95817364
Email ned@nedhalvorsen.com.au

Requirements
Must have
• Friendly but professional
Water Mark
Gloss Front

```html
<!DOCTYPE html>
<html lang="en">
<head>
<meta charset="utf-8">
<title>Ned Halvorsen – Business Card</title>
<link rel="stylesheet" href="https://fonts.googleapis.com/css2?family=Marcellus+SC&family=Arimo&family=Signika:wght@600&display=swap">
<style>
  :root {
    --page: #e4e4e4;
    --charcoal: #333333;
    --black: #050505;
    --red: #c8001a;
    --red-light: #f03a50;
    --red-deep: #b00010;
    --silver: #b9b9b9;
    --silver-dark: #6d6d6d;
    --text-grey: #bdbdbd;
    --text-light: #e6e6e6;
  }
  html, body {
    margin: 0;
    width: 1200px;
    height: 900px;
    overflow: hidden;
    background: var(--page);
  }
  .card {
    position: absolute;
    left: 75px;
    top: 150px;
    width: 1050px;
    height: 600px;
    overflow: hidden;
    box-shadow: 0 10px 30px rgba(0,0,0,0.25);
  }
  .card-art {
    position: absolute;
    inset: 0;
  }
  .identity {
    position: absolute;
    left: 60px;
    top: 280px;
    color: var(--text-grey);
  }
  .identity-name {
    margin: 0;
    font-family: "Marcellus SC", serif;
    font-weight: 400;
    font-size: 60px;
    letter-spacing: 2px;
    line-height: 1;
  }
  .identity-role {
    margin: 10px 0 0 36px;
    font-family: "Arimo", sans-serif;
    font-size: 20px;
    line-height: 1.3;
    color: #d9d0d0;
    white-space: nowrap;
  }
  .contact {
    position: absolute;
    left: 706px;
    top: 232px;
    font-family: "Arimo", sans-serif;
    font-size: 22px;
    line-height: 1.5;
    color: var(--text-light);
  }
  .contact p { margin: 0; white-space: nowrap; }
  .addresses {
    position: absolute;
    left: 30px;
    top: 488px;
    font-family: "Signika", sans-serif;
    font-weight: 600;
    font-size: 25px;
    line-height: 1.38;
    color: var(--text-grey);
  }
  .addresses p { margin: 0; white-space: nowrap; }
  .addresses .indent { padding-left: 30px; }
</style>
</head>
<body>
  <div class="card">
    <svg class="card-art" width="1050" height="600" viewBox="0 0 1050 600" aria-hidden="true">
      <defs>
        <linearGradient id="red-fill" x1="0" y1="0" x2="0" y2="1">
          <stop offset="0" stop-color="var(--red-light)"/>
          <stop offset="0.45" stop-color="var(--red)"/>
          <stop offset="1" stop-color="var(--red-deep)"/>
        </linearGradient>
        <linearGradient id="silver-fill" x1="0" y1="0" x2="1" y2="0">
          <stop offset="0" stop-color="var(--silver)"/>
          <stop offset="0.6" stop-color="var(--silver-dark)"/>
          <stop offset="1" stop-color="#3a3a3a"/>
        </linearGradient>
      </defs>
      <rect class="red-field" x="0" y="0" width="1050" height="600" fill="url(#red-fill)"/>
      <rect class="top-band" x="0" y="0" width="1050" height="46" fill="var(--charcoal)"/>
      <rect class="top-rule" x="0" y="46" width="1050" height="10" fill="url(#silver-fill)"/>
      <path class="step-rule" d="M600,192 H1050 V600 H0 V458 H680 V286 L600,242 Z" fill="url(#silver-fill)"/>
      <path class="black-field" d="M622,204 H1050 V600 H0 V472 H694 V276 L622,236 Z" fill="var(--black)"/>
      <path class="gloss" d="M0,56 H1050 V150 C820,120 640,200 420,210 C260,218 120,200 0,230 Z" fill="#ffffff" opacity="0.16"/>
    </svg>

    <div class="identity">
      <h1 class="identity-name">Ned Halvorsen</h1>
      <p class="identity-role">Clinical Psychotherapist<br>Executive Coach For Personal and Professional Success</p>
    </div>

    <div class="contact">
      <p>Phone 02 95817364</p>
      <p>Email ned@nedhalvorsen.com.au</p>
    </div>

    <div class="addresses">
      <p>Address :</p>
      <p class="indent">41 Lathom Street North Sydney&nbsp; Pellington Street Office Suite 512</p>
      <p class="indent">Tarwin office 87 Tarwin Vale Road Tarwin North Sydney Office Suite 309</p>
    </div>
  </div>
</body>
</html>
```